Web3.0 Metaverse as a Service Pitch Deck

We need our investor pitch deck to look slick and professional. It should be easy to read/view with large text (investors see hundreds of these a week).
https://www.brightkolm.com/library/4T-how-to-design-a-better-pitch-deck
Just the first 10 slides, two of which should be combined (monetization):
https://links.quorvanta.com/pitchdeckwip

```html
<!DOCTYPE html>
<html lang="en">
<head>
<meta charset="utf-8">
<title>Metaverse Web3.0 Pitch Deck</title>
<link href="https://fonts.googleapis.com/css2?family=Arimo:ital,wght@0,400;0,700;1,400;1,700&display=swap" rel="stylesheet">
<style>
  :root {
    --page: #e8e8e8;
    --slide-dark: #1e0019;
    --slide-edge: #b9b9b9;
    --hero-top: #3a0a3a;
    --hero-mid: #7b2a7b;
    --hero-low: #a35aa3;
    --city-top: #6a2fb0;
    --city-mid: #9a3fc4;
    --city-low: #3a1870;
    --plum: #4a0a44;
    --accent: #9b22a8;
    --white: #ffffff;
    --soft: #e9dde8;
    --layer-purple: #8e12f2;
    --layer-cyan: #2ef6f6;
    --layer-green: #2ed63a;
    --layer-red: #e12424;
    --layer-yellow: #ecec2a;
  }
  * { margin: 0; padding: 0; box-sizing: border-box; }
  html, body {
    width: 1200px; height: 3043px; overflow: hidden;
    background: var(--page);
    font-family: "Arimo", Arial, sans-serif;
    color: var(--white);
  }
  .deck { position: relative; width: 1200px; height: 3043px; }
  .slide {
    position: absolute; left: 102px; width: 1009px; height: 567px;
    background: var(--slide-dark); overflow: hidden;
    box-shadow: 0 0 0 1px var(--slide-edge), 0 2px 4px rgba(0,0,0,.25);
  }
  .slide-title { left: 107px; top: 48px; }
  .slide-intro { top: 647px; }
  .slide-team { top: 1246px; height: 568px; }
  .slide-money { top: 1845px; }
  .slide-layers { top: 2443px; }

  .hero-art {
    position: absolute; inset: 0;
    background:
      radial-gradient(ellipse at 50% 95%, rgba(230,170,230,.55), transparent 45%),
      linear-gradient(180deg, var(--hero-top) 0%, var(--hero-mid) 55%, var(--hero-low) 80%, var(--hero-top) 100%);
  }
  .hero-heading {
    position: absolute; left: 0; right: 0; top: 158px; text-align: center;
    font-weight: 700; font-size: 66px; letter-spacing: 1px; line-height: 1;
  }
  .hero-sub {
    position: absolute; left: 0; right: 0; top: 248px; text-align: center;
    font-weight: 700; font-size: 54px; line-height: 1;
  }

  .city-art {
    position: absolute; left: 0; top: 0; width: 100%; height: 337px;
    background:
      linear-gradient(180deg, var(--city-top) 0%, var(--city-mid) 45%, var(--city-low) 85%, #2a0c4a 100%);
  }
  .intro-badge {
    position: absolute; left: 451px; top: 292px; width: 106px; height: 106px;
    border-radius: 50%; background: var(--plum);
  }
  .intro-copy {
    position: absolute; left: 100px; right: 100px; top: 433px;
    text-align: center; font-size: 17.5px; line-height: 23px;
  }

  .section-heading {
    position: absolute; left: 0; right: 0; text-align: center;
    font-weight: 700; font-size: 41px; line-height: 1;
  }
  .slide-team .section-heading { top: 43px; }
  .slide-money .section-heading,
  .slide-layers .section-heading { top: 22px; }

  .member { position: absolute; top: 214px; width: 260px; margin-left: -130px; text-align: center; }
  .member-photo {
    width: 118px; height: 118px; margin: 0 auto;
    background: var(--plum); border-radius: 59px 0 59px 59px;
  }
  .member-name { margin-top: 14px; font-weight: 700; font-size: 18px; line-height: 22px; }
  .member-role { font-size: 15px; line-height: 20px; letter-spacing: .4px; }

  .dollar {
    position: absolute; left: 164px; top: 170px;
    font-weight: 700; font-size: 290px; line-height: 1;
  }
  .money-lines { position: absolute; inset: 0; }
  .stream { position: absolute; left: 547px; width: 330px; }
  .stream-title { color: var(--accent); font-weight: 700; font-size: 18px; line-height: 20px; }
  .stream-text { font-size: 14px; line-height: 18px; }
  .money-note {
    position: absolute; left: 174px; top: 507px; font-size: 12.5px; color: var(--soft);
  }

  .tier-summary { position: absolute; left: 0; right: 0; top: 88px; text-align: center; }
  .tier-summary .stream-title { font-size: 18px; }
  .tier-summary .stream-text { font-size: 14px; margin-top: 2px; }
  .tier { position: absolute; right: 542px; width: 330px; text-align: right; }
  .tier .stream-title { font-size: 18px; }
  .stack { position: absolute; inset: 0; }
</style>
</head>
<body>
<main class="deck">

  <section class="slide slide-title">
    <div class="hero-art" role="img" aria-label="Purple futuristic city illustration with a lone figure standing on a glowing road"></div>
    <h1 class="hero-heading">METAVERSE</h1>
    <p class="hero-sub">Web3.0</p>
  </section>

  <section class="slide slide-intro">
    <div class="city-art" role="img" aria-label="Neon purple and cyan city skyline at night with vertical light beams"></div>
    <div class="intro-badge"></div>
    <p class="intro-copy">Lorem Ipsum is simply dummy text of the printing and typesetting industry. Lorem Ipsum has been the industry's standard dummy text ever since the 1500s, when an unknown printer took a galley of type and scrambled it to make a type specimen book.</p>
  </section>

  <section class="slide slide-team">
    <h2 class="section-heading">CORE TEAM</h2>
    <div class="member" style="left:226px">
      <div class="member-photo"></div>
      <p class="member-name">Daniel Hargrove</p>
      <p class="member-role">Co-Founder, Platform Lead</p>
    </div>
    <div class="member" style="left:501px">
      <div class="member-photo"></div>
      <p class="member-name">Mark Ellery</p>
      <p class="member-role">Co-Founder, Development Lead</p>
    </div>
    <div class="member" style="left:779px">
      <div class="member-photo"></div>
      <p class="member-name">Luis Ortega</p>
      <p class="member-role">Design Lead</p>
    </div>
  </section>

  <section class="slide slide-money">
    <h2 class="section-heading">MONETIZATION</h2>
    <div class="dollar">$</div>
    <svg class="money-lines" width="1009" height="567" viewBox="0 0 1009 567">
      <defs>
        <marker id="tip" viewBox="0 0 10 10" refX="9" refY="5" markerWidth="6" markerHeight="6" orient="auto">
          <path d="M0 0 L10 5 L0 10 z" fill="#ffffff"/>
        </marker>
      </defs>
      <path d="M223 151 A157 157 0 0 1 235 464" fill="none" stroke="#ffffff" stroke-width="1.2" stroke-dasharray="5 4" opacity=".8"/>
      <g stroke="#ffffff" stroke-width="1.2" marker-end="url(#tip)">
        <line x1="371" y1="246" x2="540" y2="151"/>
        <line x1="380" y1="283" x2="536" y2="260"/>
        <line x1="377" y1="340" x2="536" y2="358"/>
        <line x1="361" y1="390" x2="536" y2="431"/>
      </g>
    </svg>
    <div class="stream" style="top:141px">
      <p class="stream-title">In-Game Tax and Microtransactions</p>
      <p class="stream-text">A large number of items, upgrades, cosmetics, and more will be made available for purchase. 1 - 6.5% Tax/Fee on all transactions.</p>
    </div>
    <div class="stream" style="top:245px">
      <p class="stream-title">Service Fees</p>
      <p class="stream-text">Basic onboarding — One-time fee of $15,000.<br>Over 20 partners.<br>Advanced onboarding — Starting at $100,000.</p>
    </div>
    <div class="stream" style="top:349px">
      <p class="stream-title">Partner Transaction Fees</p>
      <p class="stream-text">15% of all transactions made in partner spaces.</p>
    </div>
    <div class="stream" style="top:418px">
      <p class="stream-title">Extended Service Costs</p>
      <p class="stream-text"><em>A la carté</em> services and content creation —<br>Starting at $15,000.</p>
    </div>
    <p class="money-note">B2P -&gt; Variable , P2C -&gt; 2.5% tx fee, B2C -&gt; 100% Our Bankroll, Consumer to Consumer 2.5% Tax on Trans?</p>
  </section>

  <section class="slide slide-layers">
    <h2 class="section-heading">MONETIZATION</h2>
    <div class="tier-summary">
      <p class="stream-title">In-Game Tax and Microtransactions</p>
      <p class="stream-text">A large number of items, upgrades, cosmetics, and more will be made available for purchase. 1 - 6.5% Tax/Fee on all transactions.</p>
    </div>

    <svg class="stack" width="1009" height="567" viewBox="0 0 1009 567">
      <defs>
        <marker id="tipLeft" viewBox="0 0 10 10" refX="1" refY="5" markerWidth="6" markerHeight="6" orient="auto-start-reverse">
          <path d="M0 0 L10 5 L0 10 z" fill="#ffffff"/>
        </marker>
      </defs>
      <g>
        <polygon points="578,474 711,534 711,548 578,488" fill="#b4b41c"/>
        <polygon points="711,534 844,474 844,488 711,548" fill="#cfcf22"/>
        <polygon points="711,414 844,474 711,534 578,474" fill="var(--layer-yellow)"/>
      </g>
      <g>
        <polygon points="578,409 711,469 711,483 578,423" fill="#a81a1a"/>
        <polygon points="711,469 844,409 844,423 711,483" fill="#c41f1f"/>
        <polygon points="711,349 844,409 711,469 578,409" fill="var(--layer-red)"/>
      </g>
      <g>
        <polygon points="578,344 711,404 711,418 578,358" fill="#22a42c"/>
        <polygon points="711,404 844,344 844,358 711,418" fill="#28bd33"/>
        <polygon points="711,284 844,344 711,404 578,344" fill="var(--layer-green)"/>
      </g>
      <g>
        <polygon points="578,279 711,339 711,353 578,293" fill="#1fbdbd"/>
        <polygon points="711,339 844,279 844,293 711,353" fill="#27d9d9"/>
        <polygon points="711,219 844,279 711,339 578,279" fill="var(--layer-cyan)"/>
      </g>
      <g>
        <polygon points="578,214 711,274 711,288 578,228" fill="#6a0cb8"/>
        <polygon points="711,274 844,214 844,228 711,288" fill="#7a0fd6"/>
        <polygon points="711,154 844,214 711,274 578,214" fill="var(--layer-purple)"/>
      </g>
      <g stroke="#ffffff" stroke-width="1.2" marker-start="url(#tipLeft)">
        <line x1="491" y1="204" x2="709" y2="204"/>
        <line x1="491" y1="282" x2="642" y2="282"/>
        <line x1="491" y1="360" x2="642" y2="360"/>
        <line x1="491" y1="433" x2="642" y2="433"/>
        <line x1="495" y1="503" x2="646" y2="503"/>
      </g>
    </svg>

    <div class="tier" style="top:171px; right:534px">
      <p class="stream-title">In-Game Microtransactions</p>
      <p class="stream-text" style="padding-right:8px">Consumable and cosmetic items,<br>quality of life upgrades, vehicles, etc.</p>
    </div>
    <div class="tier" style="top:250px">
      <p class="stream-title">Extended and <em>a la carté</em> Services</p>
      <p class="stream-text">Consumable and cosmetic items, quality<br>of life upgrades, vehicles, etc.</p>
    </div>
    <div class="tier" style="top:328px">
      <p class="stream-title">Extended and <em>a la carté</em> Services</p>
      <p class="stream-text">Consumable and cosmetic items, quality<br>of life upgrades, vehicles, etc.</p>
    </div>
    <div class="tier" style="top:405px">
      <p class="stream-title">Extended and <em>a la carté</em> Services</p>
      <p class="stream-text">Consumable and cosmetic items, quality<br>of life upgrades, vehicles, etc.</p>
    </div>
    <div class="tier" style="top:482px">
      <p class="stream-title">Extended and <em>a la carté</em> Services</p>
      <p class="stream-text">Consumable and cosmetic items, quality<br>of life upgrades, vehicles, etc.</p>
    </div>
  </section>

</main>
</body>
</html>
```